Communication Skill: GLOW Bridge

I need a Design for a skill I teach to youth. That's why the title GLOW Bridge. GLOW stands for Thoughts, Emotions, Concerns, Hopes & Desires. Under each word are some examples that are meant to help people discuss certain things. I tried to create something myself but want something much more creative and dynamic. I have attached what I designed because it has the information I need in the design. Want it to have a techie look to it.

```html
<!DOCTYPE html>
<html lang="en">
<head>
<meta charset="utf-8">
<title>GLOW Bridge – Communication Skill</title>
<link href="https://fonts.googleapis.com/css2?family=Alfa+Slab+One&family=Open+Sans:wght@500;600&family=Source+Sans+3:wght@700&display=swap" rel="stylesheet">
<style>
  :root {
    --bg: #ffffff;
    --title: #3d3228;
    --ink: #231f20;
    --orange: #f39a1e;
    --orange-letter: #ee8a22;
    --magenta-a: #a12a8c;
    --magenta-b: #d3579f;
    --magenta-letter: #c9267f;
    --lime-a: #9bc94a;
    --lime-b: #e3e12a;
    --lime-letter: #7db52a;
    --blue: #3a97c6;
    --blue-letter: #1b8fb0;
    --disc-top: #f4f5f6;
    --disc-bottom: #d4d7da;
    --icon: #ffffff;
  }
  html, body {
    margin: 0;
    padding: 0;
    overflow: hidden;
    background: var(--bg);
  }
  .canvas {
    width: 1200px;
    height: 1092px;
    position: relative;
    overflow: hidden;
  }
  .artwork { display: block; }
  .title {
    font-family: "Alfa Slab One", "Rockwell", serif;
    font-size: 60px;
    fill: var(--title);
    letter-spacing: 2px;
  }
  .initial {
    font-family: "Alfa Slab One", "Rockwell", serif;
    font-size: 74px;
  }
  .initial--g { fill: var(--orange-letter); }
  .initial--l { fill: var(--magenta-letter); }
  .initial--o { fill: var(--lime-letter); }
  .initial--w { fill: var(--blue-letter); }
  .heading {
    font-family: "Source Sans 3", "Myriad Pro", sans-serif;
    font-weight: 700;
    font-size: 35px;
    fill: var(--ink);
    letter-spacing: 0.5px;
  }
  .prompt {
    font-family: "Open Sans", Arial, sans-serif;
    font-weight: 500;
    font-size: 16.5px;
    fill: var(--ink);
  }
  .gear--orange { fill: var(--orange); }
  .gear--magenta { fill: url(#magentaFill); }
  .gear--lime { fill: url(#limeFill); }
  .gear--blue { fill: var(--blue); }
  .disc { fill: url(#discFill); stroke: #ffffff; stroke-width: 3; filter: url(#discShadow); }
  .badge { fill: none; stroke: var(--icon); stroke-width: 3; }
  .badge--solid { fill: var(--icon); stroke: none; }
  .icon { fill: var(--icon); }
</style>
</head>
<body>
<main class="canvas">
  <svg class="artwork" width="1200" height="1092" viewBox="0 0 1100 1001" xmlns="http://www.w3.org/2000/svg" aria-labelledby="poster-title">
    <title id="poster-title">GLOW Bridge: Thoughts, Emotions, Concerns, Hopes</title>
    <defs>
      <linearGradient id="magentaFill" x1="0" y1="0" x2="1" y2="0.3">
        <stop offset="0" stop-color="#a12a8c"/>
        <stop offset="1" stop-color="#d3579f"/>
      </linearGradient>
      <linearGradient id="limeFill" x1="0" y1="0" x2="1" y2="0">
        <stop offset="0" stop-color="#9bc94a"/>
        <stop offset="1" stop-color="#e3e12a"/>
      </linearGradient>
      <linearGradient id="discFill" x1="0" y1="0" x2="0.4" y2="1">
        <stop offset="0" stop-color="#f6f7f8"/>
        <stop offset="1" stop-color="#d2d5d8"/>
      </linearGradient>
      <filter id="discShadow" x="-20%" y="-20%" width="140%" height="140%">
        <feDropShadow dx="6" dy="8" stdDeviation="7" flood-color="#000" flood-opacity="0.28"/>
      </filter>
      <g id="cogTeeth">
        <rect x="-22" y="-218" width="44" height="64" rx="3" transform="rotate(0)"/>
        <rect x="-22" y="-218" width="44" height="64" rx="3" transform="rotate(25.71)"/>
        <rect x="-22" y="-218" width="44" height="64" rx="3" transform="rotate(51.43)"/>
        <rect x="-22" y="-218" width="44" height="64" rx="3" transform="rotate(77.14)"/>
        <rect x="-22" y="-218" width="44" height="64" rx="3" transform="rotate(102.86)"/>
        <rect x="-22" y="-218" width="44" height="64" rx="3" transform="rotate(128.57)"/>
        <rect x="-22" y="-218" width="44" height="64" rx="3" transform="rotate(154.29)"/>
        <rect x="-22" y="-218" width="44" height="64" rx="3" transform="rotate(180)"/>
        <rect x="-22" y="-218" width="44" height="64" rx="3" transform="rotate(205.71)"/>
        <rect x="-22" y="-218" width="44" height="64" rx="3" transform="rotate(231.43)"/>
        <rect x="-22" y="-218" width="44" height="64" rx="3" transform="rotate(257.14)"/>
        <rect x="-22" y="-218" width="44" height="64" rx="3" transform="rotate(282.86)"/>
        <rect x="-22" y="-218" width="44" height="64" rx="3" transform="rotate(308.57)"/>
        <rect x="-22" y="-218" width="44" height="64" rx="3" transform="rotate(334.29)"/>
        <circle r="186"/>
      </g>
      <clipPath id="clipTopLeft"><rect x="0" y="0" width="528" height="537"/></clipPath>
      <clipPath id="clipTopRight"><rect x="536" y="0" width="564" height="537"/></clipPath>
      <clipPath id="clipBottomLeft"><rect x="0" y="545" width="528" height="456"/></clipPath>
      <clipPath id="clipBottomRight"><rect x="536" y="545" width="564" height="456"/></clipPath>
    </defs>

    <text class="title" x="542" y="126" text-anchor="middle">GLOW BRIDGE</text>

    <!-- Thoughts cog -->
    <g class="gear gear--orange" clip-path="url(#clipTopLeft)">
      <use href="#cogTeeth" transform="translate(360 372) rotate(8)"/>
      <rect x="360" y="372" width="170" height="167"/>
    </g>
    <!-- Emotions cog -->
    <g class="gear gear--magenta" clip-path="url(#clipTopRight)">
      <use href="#cogTeeth" transform="translate(710 375) rotate(-6)"/>
      <rect x="534" y="375" width="176" height="164"/>
    </g>
    <!-- Concerns cog -->
    <g class="gear gear--lime" clip-path="url(#clipBottomLeft)">
      <use href="#cogTeeth" transform="translate(358 720) rotate(4)"/>
      <rect x="358" y="543" width="172" height="177"/>
    </g>
    <!-- Hopes cog -->
    <g class="gear gear--blue" clip-path="url(#clipBottomRight)">
      <use href="#cogTeeth" transform="translate(710 718) rotate(10)"/>
      <rect x="534" y="543" width="176" height="175"/>
    </g>

    <!-- corner icons -->
    <g class="icon icon--thought">
      <circle cx="478" cy="503" r="13"/>
      <circle cx="494" cy="494" r="14"/>
      <circle cx="506" cy="506" r="12"/>
      <rect x="466" y="503" width="50" height="17" rx="8.5"/>
      <circle cx="498" cy="527" r="4"/>
      <circle cx="507" cy="533" r="2.5"/>
    </g>
    <circle class="badge" cx="574" cy="505" r="27"/>
    <circle class="badge--solid" cx="488" cy="582" r="29"/>
    <polygon class="icon icon--star" points="575,556 581,570 596,571 585,581 588,596 575,588 562,596 565,581 554,571 569,570"/>

    <!-- Thoughts -->
    <circle class="disc" cx="360" cy="372" r="140"/>
    <text class="initial initial--g" x="360" y="315" text-anchor="middle">G</text>
    <text class="heading" x="358" y="362" text-anchor="middle">THOUGHTS</text>
    <text class="prompt" x="358" y="390" text-anchor="middle">It seems…  I wonder…</text>
    <text class="prompt" x="358" y="413" text-anchor="middle">It’s my opinion… I believe…</text>
    <text class="prompt" x="358" y="436" text-anchor="middle">I assume… I think…</text>

    <!-- Emotions -->
    <circle class="disc" cx="710" cy="375" r="140"/>
    <text class="initial initial--l" x="710" y="315" text-anchor="middle">L</text>
    <text class="heading" x="710" y="362" text-anchor="middle">EMOTIONS</text>
    <text class="prompt" x="710" y="390" text-anchor="middle">I’m…  hopeful  worried  sad</text>
    <text class="prompt" x="710" y="413" text-anchor="middle">afraid  mad  glad happy</text>
    <text class="prompt" x="710" y="436" text-anchor="middle">confident insecure  lonely</text>
    <text class="prompt" x="704" y="459" text-anchor="middle">bothered  uncertain</text>

    <!-- Concerns -->
    <circle class="disc" cx="358" cy="720" r="140"/>
    <text class="initial initial--o" x="358" y="668" text-anchor="middle">O</text>
    <text class="heading" x="358" y="716" text-anchor="middle">CONCERNS</text>
    <text class="prompt" x="360" y="746" text-anchor="middle">I worry about…</text>
    <text class="prompt" x="360" y="769" text-anchor="middle">I’m afraid that…</text>
    <text class="prompt" x="360" y="792" text-anchor="middle">I’m nervous because…</text>
    <text class="prompt" x="362" y="815" text-anchor="middle">It bothers me that…</text>

    <!-- Hopes -->
    <circle class="disc" cx="710" cy="718" r="140"/>
    <text class="initial initial--w" x="712" y="668" text-anchor="middle">W</text>
    <text class="heading" x="712" y="716" text-anchor="middle">HOPES</text>
    <text class="prompt" x="704" y="746" text-anchor="middle">I hope…  I wish…</text>
    <text class="prompt" x="712" y="769" text-anchor="middle">It’s my desire…</text>
    <text class="prompt" x="712" y="792" text-anchor="middle">I’d like to see…</text>
    <text class="prompt" x="710" y="815" text-anchor="middle">I want…  I need…</text>
  </svg>
</main>
</body>
</html>
```